Design a kids reward chart in a3 size

Hi, we require a kids reward chart for kids design required, the chart should be on an a3 size format and be similar to the links on the bottom of the page,

Our brand name is 'yupzap' please also add this at the top as a logo

The chart will have to have space for 10 chores on the side and 7 days of the across. Along with tabs for 3 names at the top (please see examples for better understanding). We will also need a daily points total area for each day at the bottom of the and a weekly points total section underneath.

We will also need a box designed for this in a3 size and also the same box in 23 x 30cm

if you have any further questions please let us know. we will require revisions at no extra cost

We require the chart to be child friendly and colourful
Examples:
https://www.shopvelt.example/Magnetic-Behavior-Multiple-Markers-Illustrated/dp/Q93KT7LP2W/ref=sr_1_12?crid=77PQ2RZLWNXKC&keywords=kids+reward+chart&qid=9081726354&s=gateway&sprefix=kids+reward%2Caps%2C228&sr=8-12

https://www.shopvelt.example/Velmit-Learning-Responsibility-Customize-Magnetic/dp/Q58HN2TZJV/ref=sr_1_5?crid=77PQ2RZLWNXKC&keywords=kids+reward+chart&qid=9081726354&s=gateway&sprefix=kids+reward%2Caps%2C228&sr=8-5

```html
<!DOCTYPE html>
<html lang="en">
<head>
<meta charset="utf-8">
<title>yupzap – Kids Reward Chart</title>
<link rel="stylesheet" href="https://fonts.googleapis.com/css2?family=Delius&family=Fredoka:wght@600&display=swap">
<style>
  :root{
    --sky:#c9dcee;
    --ray:#ffffff;
    --red:#e3363a;
    --orange:#ee7423;
    --amber:#f19a27;
    --yellow:#f4c51b;
    --lemon:#e7dc22;
    --green:#7cba2a;
    --blue:#2b9bd9;
    --navy:#2d3f8e;
    --purple:#6c3a96;
    --violet:#8e3d9b;
    --magenta:#a7399a;
    --forest:#2f8d3c;
    --white:#ffffff;
    --ink:#333333;
  }
  html,body{margin:0;padding:0;width:1200px;height:857px;overflow:hidden;}
  body{background:var(--sky);position:relative;font-family:"Delius",cursive;}
  .sunburst{position:absolute;left:0;top:0;display:block;}
  .name-tab{position:absolute;top:65px;width:282px;height:131px;border-radius:4px;}
  .name-tab--red{left:30px;background:var(--red);}
  .name-tab--yellow{left:322px;background:var(--yellow);}
  .name-tab--blue{left:606px;background:var(--blue);}
  .name-tab .star{position:absolute;top:10px;width:26px;height:26px;}
  .name-tab .star--left{left:12px;}
  .name-tab .star--right{right:12px;}
  .name-field{position:absolute;left:48px;top:10px;width:186px;height:26px;background:var(--white);border-radius:13px;}
  .goal-line{position:absolute;left:0;right:0;top:44px;margin:0;text-align:center;font-size:18px;color:var(--ink);white-space:nowrap;}
  .goal-line .count{display:inline-block;width:40px;height:20px;background:var(--white);border-radius:10px;vertical-align:middle;}
  .reward-field{position:absolute;left:48px;top:80px;width:186px;height:26px;background:var(--white);border-radius:13px;}
  .name-tab--red .goal-line,.name-tab--blue .goal-line{color:var(--white);}
  .brand{position:absolute;left:990px;top:70px;display:flex;align-items:center;gap:12px;}
  .brand-dot{width:34px;height:34px;border-radius:50%;background:var(--red);}
  .brand-name{font-family:"Fredoka",sans-serif;font-weight:600;font-size:60px;color:var(--red);line-height:1;}
  .brand-art{position:absolute;left:960px;top:150px;width:210px;height:80px;border-radius:14px;background:linear-gradient(90deg,#e8c9a2,#f2a6a0,#9cc8e8);opacity:.7;}
  .day-head{position:absolute;top:246px;width:130px;height:40px;border-radius:8px 8px 0 0;color:var(--white);font-size:21px;text-align:center;line-height:40px;white-space:nowrap;}
  .chart{position:absolute;left:256px;top:286px;display:block;}
  .chore{position:absolute;left:34px;width:208px;height:42px;border-radius:7px;color:var(--white);font-size:18px;line-height:42px;padding-left:22px;box-sizing:border-box;white-space:nowrap;}
  .total-label{position:absolute;left:34px;width:208px;height:24px;border-radius:5px;color:var(--white);font-size:17px;line-height:24px;padding-left:12px;box-sizing:border-box;}
  .day-total{top:786px;background:var(--forest);}
  .week-total{top:818px;background:var(--red);}
  .day-total-bar{position:absolute;left:256px;top:786px;width:922px;height:24px;border-radius:12px;background:var(--forest);}
  .day-total-bar span{position:absolute;top:5px;width:104px;height:14px;background:var(--white);border-radius:2px;}
  .week-total-box{position:absolute;left:256px;top:818px;width:126px;height:24px;border-radius:6px;background:var(--red);}
  .week-total-box span{position:absolute;left:12px;top:5px;width:102px;height:14px;background:var(--white);border-radius:2px;}
</style>
</head>
<body>

<svg class="sunburst" width="1200" height="857" viewBox="0 0 1200 857" aria-hidden="true">
  <g fill="var(--ray)" opacity=".9">
    <polygon points="600,400 130,0 230,0"/>
    <polygon points="600,400 470,0 540,0"/>
    <polygon points="600,400 700,0 770,0"/>
    <polygon points="600,400 980,0 1090,0"/>
    <polygon points="600,400 1200,230 1200,320"/>
    <polygon points="600,400 0,150 0,240"/>
    <polygon points="600,400 0,380 0,450"/>
  </g>
</svg>

<section class="name-tab name-tab--red">
  <svg class="star star--left" viewBox="0 0 24 24"><path d="M12 1.5l3.1 6.6 7.2.9-5.3 5 1.4 7.1L12 17.6 5.6 21.1 7 14 1.7 9l7.2-.9z" fill="var(--white)"/></svg>
  <div class="name-field"></div>
  <svg class="star star--right" viewBox="0 0 24 24"><path d="M12 1.5l3.1 6.6 7.2.9-5.3 5 1.4 7.1L12 17.6 5.6 21.1 7 14 1.7 9l7.2-.9z" fill="var(--white)"/></svg>
  <p class="goal-line">When i get <span class="count"></span> stars, I will</p>
  <div class="reward-field"></div>
</section>
<section class="name-tab name-tab--yellow">
  <svg class="star star--left" viewBox="0 0 24 24"><path d="M12 1.5l3.1 6.6 7.2.9-5.3 5 1.4 7.1L12 17.6 5.6 21.1 7 14 1.7 9l7.2-.9z" fill="var(--white)"/></svg>
  <div class="name-field"></div>
  <svg class="star star--right" viewBox="0 0 24 24"><path d="M12 1.5l3.1 6.6 7.2.9-5.3 5 1.4 7.1L12 17.6 5.6 21.1 7 14 1.7 9l7.2-.9z" fill="var(--white)"/></svg>
  <p class="goal-line">When i get <span class="count"></span> stars, I will</p>
  <div class="reward-field"></div>
</section>
<section class="name-tab name-tab--blue">
  <svg class="star star--left" viewBox="0 0 24 24"><path d="M12 1.5l3.1 6.6 7.2.9-5.3 5 1.4 7.1L12 17.6 5.6 21.1 7 14 1.7 9l7.2-.9z" fill="var(--white)"/></svg>
  <div class="name-field"></div>
  <svg class="star star--right" viewBox="0 0 24 24"><path d="M12 1.5l3.1 6.6 7.2.9-5.3 5 1.4 7.1L12 17.6 5.6 21.1 7 14 1.7 9l7.2-.9z" fill="var(--white)"/></svg>
  <p class="goal-line">When i get <span class="count"></span> stars, I will</p>
  <div class="reward-field"></div>
</section>

<div class="brand">
  <span class="brand-name">yupzap</span>
  <span class="brand-dot"></span>
</div>
<div class="brand-art" role="img" aria-label="Illustration of cheerful children playing on the brand letters"></div>

<div class="day-head" style="left:256px;background:var(--red)">Monday</div>
<div class="day-head" style="left:388px;background:var(--orange)">Tuesday</div>
<div class="day-head" style="left:520px;background:var(--yellow)">Wednesday</div>
<div class="day-head" style="left:652px;background:var(--green)">Thursday</div>
<div class="day-head" style="left:784px;background:var(--blue)">Friday</div>
<div class="day-head" style="left:916px;background:var(--purple)">Saturday</div>
<div class="day-head" style="left:1048px;background:var(--magenta)">Sunday</div>

<svg class="chart" width="922" height="494" viewBox="0 0 922 494" aria-label="Star tracking grid">
  <defs>
    <path id="star" d="M0-11l3.2 6.7 7.3 1-5.3 5.1 1.3 7.3L0 5.6-6.5 9.1-5.2 1.8-10.5-3.3l7.3-1z"/>
    <g id="cell-box"><rect x="3" y="6" width="124" height="40" rx="6" fill="var(--white)"/></g>
    <pattern id="cell-mon" x="0" y="0" width="130" height="49" patternUnits="userSpaceOnUse">
      <use href="#cell-box"/>
      <g fill="none" stroke="var(--red)" stroke-width="1.6"><use href="#star" x="32" y="26"/><use href="#star" x="65" y="26"/><use href="#star" x="98" y="26"/></g>
    </pattern>
    <pattern id="cell-tue" x="132" y="0" width="130" height="49" patternUnits="userSpaceOnUse">
      <use href="#cell-box"/>
      <g fill="none" stroke="var(--orange)" stroke-width="1.6"><use href="#star" x="32" y="26"/><use href="#star" x="65" y="26"/><use href="#star" x="98" y="26"/></g>
    </pattern>
    <pattern id="cell-wed" x="264" y="0" width="130" height="49" patternUnits="userSpaceOnUse">
      <use href="#cell-box"/>
      <g fill="none" stroke="var(--amber)" stroke-width="1.6"><use href="#star" x="32" y="26"/><use href="#star" x="65" y="26"/><use href="#star" x="98" y="26"/></g>
    </pattern>
    <pattern id="cell-thu" x="396" y="0" width="130" height="49" patternUnits="userSpaceOnUse">
      <use href="#cell-box"/>
      <g fill="none" stroke="var(--green)" stroke-width="1.6"><use href="#star" x="32" y="26"/><use href="#star" x="65" y="26"/><use href="#star" x="98" y="26"/></g>
    </pattern>
    <pattern id="cell-fri" x="528" y="0" width="130" height="49" patternUnits="userSpaceOnUse">
      <use href="#cell-box"/>
      <g fill="none" stroke="var(--blue)" stroke-width="1.6"><use href="#star" x="32" y="26"/><use href="#star" x="65" y="26"/><use href="#star" x="98" y="26"/></g>
    </pattern>
    <pattern id="cell-sat" x="660" y="0" width="130" height="49" patternUnits="userSpaceOnUse">
      <use href="#cell-box"/>
      <g fill="none" stroke="var(--purple)" stroke-width="1.6"><use href="#star" x="32" y="26"/><use href="#star" x="65" y="26"/><use href="#star" x="98" y="26"/></g>
    </pattern>
    <pattern id="cell-sun" x="792" y="0" width="130" height="49" patternUnits="userSpaceOnUse">
      <use href="#cell-box"/>
      <g fill="none" stroke="var(--magenta)" stroke-width="1.6"><use href="#star" x="32" y="26"/><use href="#star" x="65" y="26"/><use href="#star" x="98" y="26"/></g>
    </pattern>
  </defs>
  <rect x="0" y="0" width="130" height="494" rx="6" fill="var(--red)"/>
  <rect x="0" y="0" width="130" height="490" fill="url(#cell-mon)"/>
  <rect x="132" y="0" width="130" height="494" rx="6" fill="var(--orange)"/>
  <rect x="132" y="0" width="130" height="490" fill="url(#cell-tue)"/>
  <rect x="264" y="0" width="130" height="494" rx="6" fill="var(--yellow)"/>
  <rect x="264" y="0" width="130" height="490" fill="url(#cell-wed)"/>
  <rect x="396" y="0" width="130" height="494" rx="6" fill="var(--green)"/>
  <rect x="396" y="0" width="130" height="490" fill="url(#cell-thu)"/>
  <rect x="528" y="0" width="130" height="494" rx="6" fill="var(--blue)"/>
  <rect x="528" y="0" width="130" height="490" fill="url(#cell-fri)"/>
  <rect x="660" y="0" width="130" height="494" rx="6" fill="var(--purple)"/>
  <rect x="660" y="0" width="130" height="490" fill="url(#cell-sat)"/>
  <rect x="792" y="0" width="130" height="494" rx="6" fill="var(--magenta)"/>
  <rect x="792" y="0" width="130" height="490" fill="url(#cell-sun)"/>
</svg>

<div class="chore" style="top:290px;background:var(--red)">share with others</div>
<div class="chore" style="top:339px;background:var(--orange)">drink more water</div>
<div class="chore" style="top:388px;background:var(--amber)">flush the toilet</div>
<div class="chore" style="top:437px;background:var(--yellow)">sit on the potty</div>
<div class="chore" style="top:486px;background:var(--lemon)">wash the dishes</div>
<div class="chore" style="top:535px;background:var(--green)">walked the dog</div>
<div class="chore" style="top:584px;background:var(--blue)">say sorry</div>
<div class="chore" style="top:633px;background:var(--navy)">say hi</div>
<div class="chore" style="top:682px;background:var(--purple)">say goodbye</div>
<div class="chore" style="top:731px;background:var(--violet)">clean the yard</div>

<div class="total-label day-total">DAY TOTAL</div>
<div class="day-total-bar">
  <span style="left:13px"></span><span style="left:145px"></span><span style="left:277px"></span><span style="left:409px"></span><span style="left:541px"></span><span style="left:673px"></span><span style="left:805px"></span>
</div>

<div class="total-label week-total">WEEK TOTAL</div>
<div class="week-total-box"><span></span></div>

</body>
</html>
```